A4 Informational Flyer - Summer Pathology Course

We are looking to deliver a QRM57306 Certificate IV in Pathology Summer Course Specifically aimed at current University/TAFE students studying in a health related qualification e.g. Nursing students, Medical students, Pathology students etc.

The basis around it is that our potential students will complete this shortened summer course over the Christmas, new year break 2014/2015 which will enable them to gain further skills in the health related area and they will then be able to work in the pathology field whilst still studying - instead of working a side job at Tollery's to support them.

We would like to use slogans on the flyer for engagement such as "Sick of flipping burgers?" "Are you looking to gain additional skills in a health related field" etc. anything you can come up with as the designer, is also welcomed.

Designer to include information regarding the course as follows:

Course Introduction:

This is a National Training Package and is designed to train people wishing to pursue a career in the Pathology Collection Industry.
The modules within QRM57306 Certificate IV in Pathology provide the participants with training and skills development in a range of areas including Customer Service, Pathology Collection and Techniques, Phlebotomy (blood collection), Infection Control, Occupational Health and Safety and knowledge of the disease processes associated with clients of all ages who may require Pathology Collection.

Government Funding is available for eligible students.

Fees:

Government Funded Student Fees:
Tuition: $425
If you also have a healthcare card, $85
Resources: $355

Fee For Service Student Fees:
Tuition: $2,365
Resources: $355

Method of Study:

The summer QRM57306 Certificate IV in Pathology program is run on campus at both our Blackburn and Preston training facilities. Students will attend classes two (2) days per week from 9.30am to 2.30pm. Some workbooks are required to be completed off-campus. Extensive practical experience is undertaken in the Verdant Care Academy clinical laboratories.

Course Commencement & Duration:

Course will commence late November 2014 and includes one (1) fast track week and one (1) 4 day week. Classes will conclude by the late January 2015. (Includes 2 week break over Christmas/New Year). *Subject to student numbers

Application Process:

Complete an online enrollment form via our website www.verdantcareacademy.edu.au and our student administration will contact you within 24 hours to discuss your enrollment and the next steps to secure your place on the course.
Alternatively, contact one of our friendly staff members on 03 5172 6408 for further assistance and information.

Please include our attached logos, photos for engagement etc where appropriate.
Please include our website in bold: www.verdantcareacademy.edu.au and our phone number is bold 03 5172 6408

Please also include our "TOID No. 38471" under our logo.

We would like this overall flyer/brochure to be engaging, bold, simply, easy to read for potential students. Keeping with our company colors as much as possible is a must.

Formats must be in a normal format such as PDF for printing purposes and also a JPEG, ESP format so we can use to advertise as a picture on Facebook etc.

Industry/Entity Type

Healthcare

Font styles to use
Serif

Colors
f37123
ffc214
faa54b

Requirements
Must have
• A4, 1 sided please.

Must include codes next to course title.

```html
<!DOCTYPE html>
<html lang="en">
<head>
<meta charset="utf-8">
<title>Verdant Care Academy – Summer Pathology Course</title>
<link href="https://fonts.googleapis.com/css2?family=Archivo+Black&family=Arimo:wght@400;700&family=Lato:wght@400;700;900&family=Oswald:wght@500;600&display=swap" rel="stylesheet">
<style>
  :root{
    --orange:#f37123;
    --orange-deep:#e8571f;
    --yellow:#ffc214;
    --peach:#faa54b;
    --charcoal:#3f4042;
    --slate:#5c5d60;
    --text-grey:#6a6b6e;
    --rust:#b2401a;
    --paper:#ffffff;
    --canvas:#e9e9e9;
  }
  *{margin:0;padding:0;box-sizing:border-box}
  html,body{width:960px;height:1200px;overflow:hidden;background:var(--canvas)}
  .flyer{position:absolute;left:70px;top:22px;width:820px;height:1155px;background:var(--paper);overflow:hidden;box-shadow:0 4px 18px rgba(0,0,0,.18);font-family:"Lato",sans-serif}
  .abs{position:absolute}
  .bands{position:absolute;left:0;top:0;width:820px;height:1155px}

  .hero-photo{left:300px;top:0;width:520px;height:340px;background:linear-gradient(100deg,#f4f4f2 0%,#e7e2dc 45%,#d8cfc6 75%,#c9b8ab 100%)}
  .lab-photo{left:0;top:712px;width:460px;height:330px;background:linear-gradient(90deg,#b9ccd8 0%,#d7b48a 30%,#e6e3de 60%,rgba(255,255,255,0) 100%)}

  .brand{left:60px;top:22px;width:210px;text-align:center}
  .brand-mark{width:104px;height:104px;border-radius:50%;background:var(--orange);margin:0 auto 28px}
  .brand-name{font-weight:700;font-size:27px;line-height:1.05;color:var(--slate)}
  .toid{margin-top:6px;font-weight:900;font-size:17px;color:var(--slate)}

  .headline{left:322px;top:232px;width:540px;padding:6px 0 6px 14px;background:rgba(255,255,255,.92);transform:rotate(7deg);transform-origin:left top;font-family:"Archivo Black",sans-serif;font-size:24px;line-height:1.1;color:#222}

  .fees{left:45px;top:254px;width:250px;height:388px;background:var(--yellow);border-radius:0 0 26px 26px;text-align:center;padding-top:36px;font-family:"Arimo",sans-serif;font-weight:700;color:var(--slate)}
  .fees-title{font-size:31px;margin-bottom:8px}
  .fees-note{font-size:13px;color:var(--rust);line-height:1.15}
  .fees-amount{font-size:20px;margin:6px 0}
  .fees-small{font-size:14px;line-height:1.2}
  .fees-foot{font-size:13px;color:var(--rust);margin-top:12px;line-height:1.2;padding:0 14px}

  .intro{left:314px;top:368px;width:486px;color:#fff}
  .intro-title{font-family:"Arimo",sans-serif;font-weight:700;font-size:19px;line-height:1.2}
  .intro-sub{display:flex;align-items:center;gap:10px}
  .intro-sub::after{content:"";flex:0 0 145px;height:2px;background:#fff}
  .intro p{font-weight:700;font-size:12.5px;line-height:1.3;margin-top:8px}

  .pill{left:314px;top:572px;width:362px;height:56px;border-radius:22px;background:#fff;box-shadow:inset 0 0 0 3px #d8d8d8,0 2px 4px rgba(0,0,0,.25);font-family:"Arimo",sans-serif;font-weight:700;font-size:18px;line-height:1.15;color:var(--slate);padding:7px 0 0 18px}

  .details{right:24px;top:700px;width:540px;text-align:right}
  .section-title{font-family:"Oswald",sans-serif;font-weight:600;font-size:28px;line-height:1.15;color:var(--orange-deep)}
  .rule{position:relative;height:2px;background:var(--slate);margin:3px 0 6px 100px}
  .rule::before{content:"";position:absolute;left:-4px;top:-4px;width:10px;height:10px;border-radius:50%;background:var(--slate)}
  .section-text{font-weight:700;font-size:13.5px;line-height:16.5px;color:var(--text-grey);margin-bottom:8px}
  .fine{font-weight:700;font-size:11px;color:var(--slate)}

  .footer-left{left:26px;top:1082px;color:#fff;font-weight:900;font-size:19px;line-height:1.4}
  .footer-line{display:flex;align-items:center;gap:8px}
  .footer-right{right:24px;top:1108px;color:#fff;font-weight:900;font-size:21px;display:flex;align-items:center;gap:8px}
</style>
</head>
<body>
<main class="flyer">
  <div class="abs hero-photo" role="img" aria-label="Photo of a pathology trainer presenting beside an anatomy model"></div>
  <div class="abs lab-photo" role="img" aria-label="Photo of pathology sample tubes in a laboratory rack"></div>

  <svg class="bands" viewBox="0 0 820 1155" aria-hidden="true">
    <polygon points="0,268 820,350 820,368 0,286" fill="var(--charcoal)"/>
    <polygon points="0,286 820,368 820,636 0,710" fill="var(--orange)"/>
    <polygon points="0,712 820,638 820,656 0,730" fill="var(--slate)"/>
    <polygon points="0,1030 820,1070 820,1086 0,1046" fill="var(--slate)"/>
    <polygon points="0,1052 820,1092 820,1155 0,1155" fill="var(--orange-deep)"/>
  </svg>

  <div class="abs brand">
    <div class="brand-mark"></div>
    <div class="brand-name">verdant care<br>academy</div>
    <div class="toid">TOID No. 38471</div>
  </div>

  <div class="abs headline">Earn an accredited pathology<br>qualification during your uni break!</div>

  <section class="abs fees">
    <div class="fees-title">Fees</div>
    <div class="fees-note">Government Funded<br>Student Fees*:</div>
    <div class="fees-amount">Tuition: $425</div>
    <div class="fees-small">If you also have a<br>healthcare card, $85</div>
    <div class="fees-amount">Resources: $355</div>
    <div class="fees-note">Fee For Service Student Fees:</div>
    <div class="fees-amount" style="margin-bottom:0">Tuition: $2,365</div>
    <div class="fees-amount" style="margin-top:0">Resources $355</div>
    <div class="fees-foot">*Eligibility criteria applies. Call to see if you qualify.</div>
  </section>

  <section class="abs intro">
    <div class="intro-title">QRM57306 Certificate IV in Pathology</div>
    <div class="intro-title intro-sub">course introduction:</div>
    <p>This is a National Training Package and is designed to train people wishing to pursue a career in the Pathology Collection Industry.</p>
    <p>The modules within QRM57306 Certificate IV in Pathology provide the participants with training and skills development in a range of areas including Customer Service, Pathology Collection and Techniques, Phlebotomy (blood collection), Infection Control, Occupational Health and Safety and knowledge of the disease processes associated with clients of all ages who may require Pathology Collection.</p>
  </section>

  <div class="abs pill">Designed for uni students studying<br>a health related qualification</div>

  <section class="abs details">
    <h2 class="section-title">Method of Study</h2>
    <div class="rule"></div>
    <p class="section-text">The summer pathology program is designed specifically for students studying with a health related qualification. Extensive practical experience is undertaken in our Verdant Care Academy clinical laboratories working one on one with industry experts.</p>
    <h2 class="section-title">Locations</h2>
    <div class="rule"></div>
    <p class="section-text">Ashgrove &amp; Kellan Park</p>
    <h2 class="section-title">Course Commencement &amp; Duration</h2>
    <div class="rule"></div>
    <p class="section-text" style="margin-bottom:3px">Courses will commence late November. Students attend classes twice a week from 9.30am to 2.30pm, and includes two (2) intensive study weeks. Classes conclude by end of January, and includes a two (2) week break over Christmas/New Year.</p>
    <p class="fine">*Subject to student numbers</p>
  </section>

  <div class="abs footer-left">
    <div>Enrol online at</div>
    <div class="footer-line">
      <svg width="22" height="22" viewBox="0 0 22 22" aria-hidden="true" fill="none" stroke="#fff" stroke-width="1.8">
        <circle cx="11" cy="11" r="9"/><ellipse cx="11" cy="11" rx="4" ry="9"/><line x1="2" y1="11" x2="20" y2="11"/><path d="M4 6h14M4 16h14"/>
      </svg>
      <span>www.verdantcareacademy.edu.au</span>
    </div>
  </div>

  <div class="abs footer-right">
    <svg width="22" height="22" viewBox="0 0 22 22" aria-hidden="true">
      <rect width="22" height="22" rx="4" fill="#fff"/>
      <path d="M7 4.5c.6 0 1 .3 1.2.8l1 2.4c.2.5 0 1-.4 1.3l-1 .8c.7 1.6 2 2.9 3.6 3.6l.8-1c.3-.4.8-.6 1.3-.4l2.4 1c.5.2.8.6.8 1.2v1.8c0 .7-.6 1.3-1.3 1.3C9.3 17.3 4.7 12.7 4.7 6.8c0-.7.6-1.3 1.3-1.3z" fill="var(--orange-deep)"/>
    </svg>
    <span>03 5172 6408</span>
  </div>
</main>
</body>
</html>
```